Website for KRV GROUND

looking for a clean crisp website outlining what we do, we are a telecommunications cable installer working on internet cabling, i am just looking for imagery and we will complete content

i need a

home page template
services tab (4 services)
Rod / Roping
Hauling
Civil
Surveying
Contact Us Page
Testimonials Page
About Us
Our Vision
History

Target Market(s)

Telecommunication Companies

Industry/Entity Type

Telecommunications

Requirements
Must have
• images and logo themed colors

this is main project we are working on

http://www.wexlarnet.com.au/

this is an example of our competitor site in the same field, we are much smaller though

```html
<!DOCTYPE html>
<html lang="en">
<head>
<meta charset="utf-8">
<title>KRV GROUND – Telecommunication Cable Installers</title>
<link rel="stylesheet" href="https://fonts.googleapis.com/css2?family=Roboto:ital,wght@0,400;0,500;0,700;1,700;1,900&family=Ubuntu:wght@500;700&family=Dosis:wght@500&display=swap">
<style>
  :root {
    --brand-blue: #0f4a8f;
    --brand-blue-dark: #0b3f7d;
    --accent-blue: #0d5cb0;
    --orange: #f2921f;
    --orange-text: #ee7a0c;
    --nav-beige: #e7e0d7;
    --nav-beige-light: #f3eee8;
    --band-dark: #1d1d1f;
    --ink: #333;
    --muted: #666;
    --tile-blue: #d9eefc;
    --tile-blue-strong: #a9dbf8;
    --quote-bg: #fdf3e6;
    --quote-border: #f6dcb6;
    --rule: #cfcfcf;
  }
  * { box-sizing: border-box; margin: 0; padding: 0; }
  html, body { width: 1200px; height: 1142px; overflow: hidden; background: #fff; }
  body { position: relative; font-family: "Roboto", Arial, sans-serif; color: var(--ink); }
  a { color: inherit; text-decoration: none; }
  .abs { position: absolute; }

  /* Header */
  .site-header { left: 0; top: 0; width: 1200px; height: 127px;
    background: linear-gradient(90deg, var(--brand-blue-dark), var(--brand-blue) 50%, #124f94); }
  .brand { left: 188px; top: 30px; display: flex; align-items: center; gap: 12px; }
  .brand-mark { width: 18px; height: 18px; border-radius: 50%; background: var(--orange); }
  .brand-name { font-family: "Roboto", sans-serif; font-weight: 700; font-size: 44px; letter-spacing: 1px; color: #eef1f5; line-height: 1; }
  .top-links { right: 187px; top: 7px; font-size: 13px; color: #fff; }
  .top-links span { margin: 0 5px; font-size: 10px; }
  .follow { right: 187px; top: 103px; display: flex; align-items: center; gap: 9px; font-size: 11.5px; color: #dce6f2; }
  .follow i { width: 17px; height: 17px; display: block; border-radius: 2px; background: #c9d7e8; }
  .follow .label { margin-right: 5px; }

  /* Navigation */
  .band-top { left: 0; top: 127px; width: 1200px; height: 5px; background: var(--band-dark); }
  .main-nav { left: 0; top: 132px; width: 1200px; height: 34px;
    background: linear-gradient(var(--nav-beige-light), var(--nav-beige)); }
  .main-nav ul { list-style: none; display: flex; position: absolute; left: 184px; top: 0; height: 34px; border-left: 1px solid #cfc6ba; }
  .main-nav li { width: 78px; height: 34px; border-right: 1px solid #cfc6ba; font-family: "Dosis", sans-serif; font-weight: 500; font-size: 15px; color: #6b625a; display: flex; align-items: center; justify-content: center; }
  .main-nav li.active { background: #fbf9f6; color: #222; width: 78px; }
  .band-bottom { left: 0; top: 166px; width: 1200px; height: 7px; background: var(--band-dark); }

  /* Hero */
  .hero { left: 0; top: 173px; width: 1200px; height: 316px;
    background: radial-gradient(ellipse at 60% 60%, #f4ede6 0%, #d9cbbd 45%, #b8a596 75%, #8e7f76 100%); }
  .hero-title { left: 183px; top: 244px; font-style: italic; font-weight: 900; font-size: 21px; line-height: 28px; color: #1760c2; text-shadow: 0 1px 0 #fff, 1px 0 0 #fff, -1px 0 0 #fff, 0 -1px 0 #fff; }
  .hero-btn { left: 184px; top: 320px; height: 24px; width: 129px; display: flex; background: #4f4f4f; color: #fff; font-size: 11.5px; }
  .hero-btn span { flex: 1; padding-left: 9px; line-height: 24px; }
  .hero-btn b { width: 24px; background: #13519d; display: flex; align-items: center; justify-content: center; }

  /* Services */
  .services { left: 184px; top: 508px; width: 832px; height: 114px; display: flex; box-shadow: 0 14px 12px -12px rgba(0,0,0,.35); }
  .service { flex: 1; border-right: 1px solid #b8dcf3; background: linear-gradient(var(--tile-blue), #cfe8fa);
    display: flex; flex-direction: column; align-items: center; padding-top: 16px; }
  .service:first-child { background: linear-gradient(var(--tile-blue-strong), #bfe3fa); }
  .service:last-child { border-right: 0; }
  .service svg { height: 56px; }
  .service h3 { font-family: "Ubuntu", sans-serif; font-weight: 700; font-size: 15.5px; color: #12509a; margin-top: 11px; }

  /* About */
  .section-title { font-size: 19px; font-weight: 400; color: var(--accent-blue); }
  .about-title { left: 184px; top: 660px; }
  .about-rule { left: 184px; top: 692px; width: 488px; height: 1px; background: #555; }
  .about-image { left: 181px; top: 708px; width: 169px; height: 99px; background: linear-gradient(135deg, #eef0f7, #d9c27c 50%, #cbd1e6); box-shadow: 0 1px 4px rgba(0,0,0,.25); border: 3px solid #fff; }
  .about-text { font-size: 11.5px; line-height: 21.5px; color: #333; }
  .about-intro { left: 360px; top: 709px; width: 312px; }
  .about-more { left: 183px; top: 818px; width: 490px; }

  /* Testimonials */
  .testi-title { left: 699px; top: 660px; }
  .quote { left: 696px; top: 693px; width: 320px; height: 108px; background: var(--quote-bg); border: 1px solid var(--quote-border); border-radius: 4px; }
  .quote p { padding: 20px 12px 0 12px; font-family: "Ubuntu", sans-serif; font-weight: 500; font-size: 12px; line-height: 17px; color: var(--orange-text); }
  .quote-tail { left: 995px; top: 798px; }
  .person-photo { left: 902px; top: 783px; width: 86px; height: 77px; border: 2px solid var(--orange); background: linear-gradient(#dcd7d2, #8d7a6d); }
  .person-name { right: 309px; top: 813px; font-weight: 500; font-size: 12.5px; color: var(--accent-blue); text-align: right; }
  .person-role { right: 309px; top: 834px; font-size: 11px; color: #555; text-align: right; }

  /* Footer links */
  .footer-rule { left: 184px; top: 905px; width: 832px; height: 1px; background: #dcdcdc; }
  .link-col { top: 926px; width: 146px; }
  .link-col h4 { font-size: 14.5px; font-weight: 500; color: #444; padding-bottom: 9px; border-bottom: 1px solid var(--orange); }
  .link-col ul { list-style: none; margin-top: 10px; }
  .link-col li { font-size: 11px; line-height: 25.7px; color: #666; }

  /* Bottom bar */
  .bottom-bar { left: 0; top: 1111px; width: 1200px; height: 31px; background: var(--orange); color: #fff; font-size: 9.5px; }
  .copyright { left: 185px; top: 10px; }
  .bottom-follow { right: 184px; top: 7px; display: flex; align-items: center; gap: 5px; }
  .bottom-follow i { display: block; width: 15px; height: 15px; background: #fff; opacity: .9; border-radius: 2px; }
  .bottom-follow .label { margin-right: 6px; }
</style>
</head>
<body>

<header class="site-header abs">
  <a class="brand abs" href="#"><span class="brand-mark"></span><span class="brand-name">KRV GROUND</span></a>
  <nav class="top-links abs"><a href="#">Contact us</a><span>|</span><a href="#">Testamonials</a></nav>
  <div class="follow abs"><span class="label">Follow us</span><i></i><i></i><i></i><i></i></div>
</header>

<div class="band-top abs"></div>
<nav class="main-nav abs">
  <ul>
    <li class="active">Home</li>
    <li>About us</li>
    <li>Our vision</li>
    <li>History</li>
  </ul>
</nav>
<div class="band-bottom abs"></div>

<section class="hero abs" role="img" aria-label="Photo of hands holding a bank card while typing on a white laptop"></section>
<h1 class="hero-title abs">Connect your home<br>or your Bussiness to KRV</h1>
<a class="hero-btn abs" href="#"><span>View more</span><b><svg width="8" height="12" viewBox="0 0 8 12"><path d="M1.5 1 6.5 6 1.5 11" fill="none" stroke="#fff" stroke-width="2"/></svg></b></a>

<section class="services abs">
  <div class="service">
    <svg viewBox="0 0 64 56" width="64"><path d="M26 42 A16 16 0 1 1 40 24 A10 10 0 1 1 24 18" fill="none" stroke="#0d58a8" stroke-width="4" stroke-linecap="round"/><rect x="36" y="32" width="20" height="12" rx="3" transform="rotate(-25 46 38)" fill="#0d58a8"/></svg>
    <h3>Rod / Roping</h3>
  </div>
  <div class="service">
    <svg viewBox="0 0 56 56" width="56"><path d="M28 6 4 28h6v24h36V28h6z" fill="#0d58a8"/><path d="M28 14 14 27v21h28V27z" fill="#d9eefc"/><rect x="20" y="30" width="12" height="18" fill="#0d58a8"/><rect x="34" y="30" width="6" height="6" fill="#0d58a8"/></svg>
    <h3>Hauling</h3>
  </div>
  <div class="service">
    <svg viewBox="0 0 56 56" width="56"><circle cx="21" cy="22" r="7" fill="#0d58a8"/><circle cx="36" cy="19" r="7" fill="#0d58a8"/><path d="M8 48c0-10 6-16 13-16s13 6 13 16z" fill="#0d58a8"/><path d="M28 30c2-2 5-3 8-3 7 0 12 6 12 14h-14z" fill="#0d58a8"/></svg>
    <h3>Civil</h3>
  </div>
  <div class="service">
    <svg viewBox="0 0 64 64" width="64"><circle cx="26" cy="10" r="4" fill="#0d58a8"/><path d="M22 16 12 30 10 60h5l2-24 8-8" fill="none" stroke="#0d58a8" stroke-width="5" stroke-linejoin="round"/><rect x="32" y="10" width="16" height="6" fill="#0d58a8"/><path d="M40 18 30 60M40 18 50 60M40 18v42" stroke="#0d58a8" stroke-width="2.5"/></svg>
    <h3>Surveying</h3>
  </div>
</section>

<h2 class="section-title about-title abs">About KRV Ground</h2>
<div class="about-rule abs"></div>
<div class="about-image abs" role="img" aria-label="Photo of yellow network cables with connectors"></div>
<p class="about-text about-intro abs">As soon as the Wexlar rollout map showed my area had service available I signed up. There was a 2 week delay between ordering the service and my installation date (the installers said they are flat out doing installs).</p>
<p class="about-text about-more abs">As soon as the Wexlar rollout map showed my area had service available I signed up. There was a week delay between ordering the service and my installation date (the installers said they are flat out doing installs).</p>

<h2 class="section-title testi-title abs">Testamonials</h2>
<div class="quote abs"><p>Nam eleifend odio id sapien dignissim et convallis est rhoncus. Sed volutpat,</p></div>
<svg class="quote-tail abs" width="22" height="30" viewBox="0 0 22 30"><path d="M0 0h20L2 28z" fill="#fdf3e6"/><path d="M20 0 2 28" stroke="#f6dcb6" fill="none"/></svg>
<div class="person-photo abs" role="img" aria-label="Portrait photo of the client"></div>
<p class="person-name abs">Mrs Delphine</p>
<p class="person-role abs">Ceo at innovative Comp.</p>

<div class="footer-rule abs"></div>
<div class="link-col abs" style="left:184px"><h4>KRV links</h4><ul><li>Delivery &amp; returns</li><li>Extensions &amp; replacement</li><li>vouchers</li><li>Availablity &amp; your voucher</li><li>UK-wide locations</li></ul></div>
<div class="link-col abs" style="left:356px"><h4>Categories</h4><ul><li>Delivery &amp; returns</li><li>Extensions &amp; replacement</li><li>vouchers</li><li>Availablity &amp; your voucher</li><li>UK-wide locations</li></ul></div>
<div class="link-col abs" style="left:525px"><h4>Categories</h4><ul><li>Delivery &amp; returns</li><li>Extensions &amp; replacement</li><li>vouchers</li><li>Availablity &amp; your voucher</li><li>UK-wide locations</li></ul></div>
<div class="link-col abs" style="left:696px"><h4>Categories</h4><ul><li>Delivery &amp; returns</li><li>Extensions &amp; replacement</li><li>vouchers</li><li>Availablity &amp; your voucher</li><li>UK-wide locations</li></ul></div>
<div class="link-col abs" style="left:870px"><h4>Categories</h4><ul><li>Delivery &amp; returns</li><li>Extensions &amp; replacement</li><li>vouchers</li><li>Availablity &amp; your voucher</li><li>UK-wide locations</li></ul></div>

<footer class="bottom-bar abs">
  <span class="copyright abs">All Content Copyright 2012 - All Rights Reserved.</span>
  <div class="bottom-follow abs"><span class="label">Follow us</span><i></i><i></i><i></i><i></i></div>
</footer>

</body>
</html>
```